Corvana Wound Care Business card design

We need a business card designed around our logo which was provided. The logo of preference is the colored. Also the colors and fonts were provided.

Target Market(s)

Our Referral partners are home health agencies.

Industry/Entity Type

Healthcare

Contact Information for Business Card

Name , Phone #, Email , Title

Requirements
Nice to have
• Creativity
Should not have
• basic

```html
<!DOCTYPE html>
<html lang="en">
<head>
<meta charset="UTF-8">
<title>Corvana Wound Care – Business Card</title>
<link href="https://fonts.googleapis.com/css2?family=Poppins:wght@400;500;600&display=swap" rel="stylesheet">
<style>
  :root {
    --navy: #123f86;
    --deep-bg: #0b3566;
    --deep-bg-edge: #072549;
    --sky: #0aa2e2;
    --white: #ffffff;
    --ink-soft: #1d4a93;
  }
  * { margin: 0; padding: 0; box-sizing: border-box; }
  html, body { width: 1200px; height: 900px; overflow: hidden; }
  body {
    background: radial-gradient(ellipse at 50% 45%, var(--deep-bg) 0%, var(--deep-bg-edge) 100%);
    font-family: "Poppins", sans-serif;
    position: relative;
  }
  .card {
    position: absolute;
    left: 230px;
    width: 740px;
    height: 420px;
    overflow: hidden;
    box-shadow: 0 18px 40px rgba(0, 0, 0, 0.35);
  }
  .card-front { top: 20px; background: var(--white); }
  .card-back { top: 460px; background: var(--sky); }

  .brand {
    display: flex;
    align-items: center;
    gap: 12px;
    font-weight: 600;
    white-space: nowrap;
  }
  .brand-square { display: block; }
  .card-front .brand {
    position: absolute;
    top: 48px;
    right: 56px;
    font-size: 24px;
    color: var(--navy);
  }
  .card-front .brand-square { width: 22px; height: 22px; background: var(--navy); }

  .rule { position: absolute; }
  .rule-top-thin { top: 126px; left: 330px; right: 0; height: 2px; background: var(--sky); }
  .rule-top-thick { top: 123px; left: 560px; right: 0; height: 7px; background: var(--sky); }
  .rule-mid-thick { top: 262px; left: 0; width: 470px; height: 6px; background: var(--navy); }
  .rule-mid-thin { top: 264px; left: 470px; right: 0; height: 2px; background: var(--navy); }

  .person {
    position: absolute;
    top: 180px;
    left: 60px;
    display: flex;
    flex-direction: column;
    align-items: flex-end;
  }
  .person-name { font-size: 30px; font-weight: 500; color: var(--navy); line-height: 1.1; }
  .person-title {
    font-size: 13px;
    font-weight: 500;
    color: var(--sky);
    letter-spacing: 0.5px;
    text-transform: uppercase;
    margin-top: 4px;
  }

  .contact-list {
    position: absolute;
    top: 296px;
    left: 80px;
    list-style: none;
  }
  .contact-item {
    display: flex;
    align-items: center;
    gap: 16px;
    font-size: 25px;
    font-weight: 500;
    color: var(--ink-soft);
    margin-bottom: 14px;
  }
  .contact-icon { width: 32px; height: 32px; flex: none; }

  .card-back .brand {
    position: absolute;
    top: 50%;
    left: 50%;
    transform: translate(-50%, -50%);
    font-size: 48px;
    gap: 20px;
    color: var(--white);
  }
  .card-back .brand-square { width: 44px; height: 44px; background: var(--navy); }
</style>
</head>
<body>
  <section class="card card-front" aria-label="Business card front">
    <div class="brand"><span class="brand-square"></span>Corvana Wound Care</div>
    <div class="rule rule-top-thin"></div>
    <div class="rule rule-top-thick"></div>

    <div class="person">
      <p class="person-name">Name : Dr. Halvren</p>
      <p class="person-title">General Surgeon</p>
    </div>
    <div class="rule rule-mid-thick"></div>
    <div class="rule rule-mid-thin"></div>

    <ul class="contact-list">
      <li class="contact-item">
        <svg class="contact-icon" viewBox="0 0 32 32" aria-hidden="true">
          <circle cx="16" cy="16" r="16" fill="#0aa2e2"/>
          <path d="M11 9.5c.8-.6 1.8-.4 2.3.4l1.3 2.2c.4.7.2 1.5-.4 2l-1 .8c.8 1.8 2.1 3.2 3.9 4l.8-1c.5-.6 1.3-.8 2-.4l2.2 1.3c.8.5 1 1.5.4 2.3l-.9 1.1c-.8 1-2.2 1.3-3.4.8-3.8-1.6-6.8-4.6-8.4-8.4-.5-1.2-.2-2.6.8-3.4z" fill="none" stroke="#fff" stroke-width="1.6" stroke-linejoin="round"/>
        </svg>
        <span>555-014-2837</span>
      </li>
      <li class="contact-item">
        <svg class="contact-icon" viewBox="0 0 32 32" aria-hidden="true">
          <circle cx="16" cy="16" r="16" fill="#0aa2e2"/>
          <rect x="8.5" y="10.5" width="15" height="11" rx="1.5" fill="none" stroke="#fff" stroke-width="1.6"/>
          <path d="M9 11.5l7 5.5 7-5.5" fill="none" stroke="#fff" stroke-width="1.6" stroke-linejoin="round"/>
        </svg>
        <span>halvren@corvanacare.co</span>
      </li>
    </ul>
  </section>

  <section class="card card-back" aria-label="Business card back">
    <div class="brand"><span class="brand-square"></span>Corvana Wound Care</div>
  </section>
</body>
</html>
```